Ferncrest Dental, LLC business card project

Business card to be designed with current logo.
Dental office- please keep design of card that looks clean and professional.
Please include the following info:
Ferncrest Dental, LLC
Dr. Lorna Pettigrew
2871 Marlowe Street
Lindenvale, NT 18093
555-555-0193
ferncrestdental.office@examplemail.test
Hello everyone-
Reason: Just got back from overseas- will look at all designs and provide feedback. Thank you!
Reason: Polling my friends for the final selection-
thank you to all those that participated- so many talented designers!

```html
<!DOCTYPE html>
<html lang="en">
<head>
<meta charset="utf-8">
<title>Ferncrest Dental, LLC — Business Card</title>
<link rel="stylesheet" href="https://fonts.googleapis.com/css2?family=Quicksand:wght@400&family=Arimo:wght@400;700&display=swap">
<style>
  :root {
    --backdrop: #ecebe8;
    --card-white: #ffffff;
    --green-deep: #66a043;
    --green-lime: #b3d235;
    --brand-green: #6aa545;
    --mist: #efefef;
    --ink: #1a1a1a;
    --text-green: #4f9134;
  }
  * { margin: 0; padding: 0; box-sizing: border-box; }
  html, body { width: 1200px; height: 900px; overflow: hidden; }
  body { background: var(--backdrop); position: relative; font-family: "Arimo", Arial, sans-serif; }

  .card {
    position: absolute;
    width: 520px;
    height: 300px;
    overflow: hidden;
    box-shadow: 0 3px 10px rgba(0,0,0,0.18);
  }
  .card__shapes { position: absolute; inset: 0; width: 100%; height: 100%; }

  .card--front { left: 580px; top: 90px; background: var(--card-white); }
  .card--back { left: 120px; top: 500px; background: var(--green-deep); }

  .brand {
    position: absolute;
    display: flex;
    align-items: center;
    gap: 10px;
    font-family: "Quicksand", "Century Gothic", sans-serif;
    font-weight: 400;
    white-space: nowrap;
  }
  .brand__dot { width: 14px; height: 14px; border-radius: 50%; }

  .card--front .brand { left: 36px; top: 58px; font-size: 28px; color: var(--brand-green); }
  .card--front .brand__dot { background: var(--brand-green); }

  .card--back .brand { left: 0; right: 0; top: 128px; justify-content: center; font-size: 34px; color: #ffffff; }
  .card--back .brand__dot { background: #ffffff; width: 16px; height: 16px; }

  .address {
    position: absolute;
    left: 36px;
    top: 132px;
    font-size: 13px;
    font-style: normal;
    line-height: 1.35;
    color: var(--text-green);
  }
  .contact {
    position: absolute;
    left: 278px;
    top: 176px;
    font-size: 12px;
    line-height: 1.4;
    color: var(--text-green);
  }
  .contact__name {
    font-size: 14px;
    font-weight: 700;
    color: var(--ink);
    margin-bottom: 3px;
  }
</style>
</head>
<body>

  <section class="card card--front" aria-label="Business card front">
    <svg class="card__shapes" viewBox="0 0 520 300" preserveAspectRatio="none" aria-hidden="true">
      <path fill="var(--green-lime)" d="M40,0 H520 V92 C400,48 210,14 40,0 Z"/>
      <path fill="var(--green-deep)" d="M40,0 H520 V58 C400,30 210,9 40,0 Z"/>
      <path fill="var(--green-lime)" d="M0,246 C200,242 380,258 520,292 V300 H0 Z"/>
      <path fill="var(--green-deep)" d="M0,262 C210,262 390,266 520,248 V300 H0 Z"/>
    </svg>

    <div class="brand">
      <span class="brand__dot"></span>
      <span class="brand__name">Ferncrest Dental, LLC</span>
    </div>

    <address class="address">
      2871 Marlowe Street,<br>
      Lindenvale, NT 18093.
    </address>

    <div class="contact">
      <p class="contact__name">Dr. Lorna Pettigrew</p>
      <p class="contact__phone">555-555-0193</p>
      <p class="contact__email">ferncrestdental.office@examplemail.test</p>
    </div>
  </section>

  <section class="card card--back" aria-label="Business card back">
    <svg class="card__shapes" viewBox="0 0 520 300" preserveAspectRatio="none" aria-hidden="true">
      <path fill="var(--mist)" d="M0,0 H520 V28 C360,40 160,58 0,82 Z"/>
      <path fill="var(--mist)" d="M0,246 C180,222 380,214 520,232 V300 H0 Z"/>
    </svg>

    <div class="brand">
      <span class="brand__dot"></span>
      <span class="brand__name">Ferncrest Dental, LLC</span>
    </div>
  </section>

</body>
</html>
```